Window film company looking for a visually appealing box design to ship out products with.

We need a new box design for our window film products. We will provide images of our previous box design as an example. The design we are looking for should have a bold and luxurious tone to it. Our Company name, "Halbrook Window Films," should also be easily showcased with an Emphasis on "Halbrook". We need to have an ulta modern techy vibe in the box design. We want to make sure its simple but has the blue pop. The designs we showed you are examples but i think they have to much going on and i want something more simple.

Target Market(s)

Window film Industry

Font styles to use
Other font styles liked:
• I want a font similar to the "vossen font" RED image below.

Requirements
Must have
• Company name : HALBROOK
WEBSITE: www.halbrookdistributors.com
Youtube: Halbrook
facebook:HalbrookDistribution
Instagram: HalbrookDistribution

COLOR CODE OF OUR BUSINESS : MUST MATCH THE BLUE IN OUR COMPANY LOGO. (HALBROOK DISTIBUTION)

RGB:
Red: 84
Green:200
blue:232
Nice to have
• I would need to have a modern look. More of a dark vibe.
Should not have
• Any other colors besides our company colors.

```html
<!DOCTYPE html>
<html lang="en">
<head>
<meta charset="utf-8">
<title>Halbrook Window Films – Box Dieline</title>
<link rel="stylesheet" href="https://fonts.googleapis.com/css2?family=Orbitron:wght@500;600&display=swap">
<style>
  :root {
    --backdrop: #93e6fb;
    --brand-blue: #54c8e8;
    --panel-blue: #52c6e7;
    --fold-line: #9fe3f6;
    --carbon: #222326;
    --ink: #1d1e20;
    --white: #ffffff;
  }
  html, body {
    margin: 0;
    width: 829px;
    height: 1200px;
    overflow: hidden;
    background: var(--backdrop);
  }
  .dieline {
    position: absolute;
    left: 24px;
    top: 377px;
    width: 781px;
    height: 446px;
  }
  .dieline text {
    font-family: "Orbitron", sans-serif;
  }
  .panel { fill: var(--panel-blue); }
  .fold { stroke: var(--fold-line); stroke-width: 3; }
  .carbon-band { fill: var(--carbon); stroke: var(--white); stroke-width: 4; stroke-linejoin: round; }
  .trim-line { fill: none; stroke: var(--white); stroke-width: 4; stroke-linejoin: round; }
  .wordmark-large { fill: var(--brand-blue); font-size: 58px; font-weight: 600; }
  .tagline { fill: var(--white); font-size: 26px; font-weight: 500; }
  .website { fill: var(--brand-blue); font-size: 17px; font-weight: 500; }
  .brand-name { fill: var(--ink); font-weight: 600; }
  .social-handle { fill: var(--ink); font-size: 19px; font-weight: 500; }
  .social-mark { fill: var(--white); }
  .brand-mark { fill: none; stroke: var(--white); stroke-width: 5; }
</style>
</head>
<body>
<svg class="dieline" viewBox="0 0 1507 861" xmlns="http://www.w3.org/2000/svg" aria-label="Halbrook Window Films box dieline">
  <defs>
    <g id="side-panel">
      <line class="trim-line" x1="215" y1="33" x2="1292" y2="33"/>
      <polygon class="carbon-band" points="500,33 1035,33 1015,70 470,70"/>
      <polyline class="trim-line" points="215,73 255,73"/>
      <path class="carbon-band" d="M255 73 H540 L530 90 H265 Z"/>
      <path class="trim-line" d="M1090 73 L1102 52 H1275 L1290 73"/>
      <path class="trim-line" d="M695 165 L683 145 H325 L312 165"/>
      <path class="carbon-band" d="M215 215 V165 H725 L765 105 H1294 V217 Z"/>
      <text class="wordmark-large" x="855" y="165" textLength="430" lengthAdjust="spacingAndGlyphs">HALBROOK</text>
      <text class="tagline" x="990" y="192" textLength="297" lengthAdjust="spacingAndGlyphs">WINDOW FILMS</text>
      <text class="website" x="250" y="200" textLength="365" lengthAdjust="spacingAndGlyphs">WWW.HALBROOKDISTRIBUTORS.COM</text>
    </g>
  </defs>

  <rect class="panel" x="0" y="0" width="1507" height="861"/>
  <line class="fold" x1="0" y1="215" x2="215" y2="215"/>
  <line class="fold" x1="1292" y1="215" x2="1507" y2="215"/>
  <line class="fold" x1="0" y1="430" x2="215" y2="430"/>
  <line class="fold" x1="1292" y1="430" x2="1507" y2="430"/>
  <line class="fold" x1="0" y1="645" x2="215" y2="645"/>
  <line class="fold" x1="1292" y1="645" x2="1507" y2="645"/>

  <g class="top-panel" transform="rotate(180 753.5 107.5)">
    <use href="#side-panel"/>
  </g>

  <g class="front-panel">
    <rect class="brand-mark" x="280" y="277" width="100" height="92"/>
    <text class="brand-name" x="407" y="324" font-size="40" textLength="305" lengthAdjust="spacingAndGlyphs">HALBROOK</text>
    <text class="brand-name" x="435" y="348" font-size="17" textLength="248" lengthAdjust="spacingAndGlyphs">DISTRIBUTION</text>

    <text class="social-handle" x="1200" y="293" text-anchor="end">HALBROOK</text>
    <rect class="social-mark" x="1207" y="274" width="22" height="22" rx="4"/>
    <text class="social-handle" x="1200" y="331" text-anchor="end">HALBROOKDISTRIBUTION</text>
    <rect class="social-mark" x="1207" y="312" width="22" height="22" rx="4"/>
    <text class="social-handle" x="1200" y="369" text-anchor="end">HALBROOKDISTRIBUTION</text>
    <rect class="social-mark" x="1207" y="350" width="22" height="22" rx="4"/>
  </g>

  <g class="bottom-panel" transform="translate(0 430)">
    <use href="#side-panel"/>
  </g>
</svg>
</body>
</html>
```